Business Card Design Project for Female Personal Trainer

I need a business card design to appeal to female clients for my personal training and group fitness boot camp business called 'LumaStride Studio'. It should be girly, fun and have an active/healthy pic or figure incorporated into the business name.

Target Market(s)

- Females 20-65yrs

Industry/Entity Type

Training

Font styles to use
Serif
Sans Serif

Colors
e34197
e567a6

Requirements
Must have
• First Side of Business Card Details :

Odette Calvo
MASTER PERSONAL TRAINER
Cert III & Cert IV in Fitness
Senior First Aid
Mobile: 0493 507 618
Email: lumastride@quellmail.test
Facebook: LumaStride Studio

* Mobile Personal Training *Individual Sessions *Bootcamp *Weight-loss and Toning

Second Side of Business Card I want to offer a free personal consult:
Something like this:

Need direction with your health & fitness goals?

Call now for your free 1 on 1 Personal Training Session with full consultation

Nice to have
• Have a sub-heading for example:

'Promoting healthy living through fitness & nutrition'

- have the colour pink or blue (to appeal to a female)

- a picture/motif//logo attached (sometimes a picture paints a thousand words)

Should not have
• * picture of a person with big muscles or appeal to a man (I'm training women only)

* should not be busy or crammed up look (if I've added to much info above please just use to your discretion).

```html
<!DOCTYPE html>
<html lang="en">
<head>
<meta charset="utf-8">
<title>LumaStride Studio – Free Consultation Card</title>
<link rel="stylesheet" href="https://fonts.googleapis.com/css2?family=Courgette&family=Libre+Baskerville:ital,wght@1,700&display=swap">
<style>
  :root {
    --paper: #ffffff;
    --ink-title: #3f73bf;
    --ink-body: #2d5ea9;
    --bullet: #111111;
    --ornament: #2f5fa8;
    --ornament-soft: #6f95d0;
  }
  * { margin: 0; padding: 0; box-sizing: border-box; }
  html, body {
    width: 1200px;
    height: 686px;
    overflow: hidden;
    background: var(--paper);
  }
  .card {
    position: relative;
    width: 1200px;
    height: 686px;
    background: var(--paper);
    overflow: hidden;
  }
  .corner-flourish { position: absolute; }
  .corner-flourish--top-left {
    left: 0; top: 0;
    width: 150px; height: 90px;
    background: radial-gradient(ellipse at top left, var(--ornament) 0%, var(--ornament-soft) 55%, rgba(255,255,255,0) 75%);
  }
  .corner-flourish--bottom-right {
    right: 0; bottom: 0;
    width: 125px; height: 135px;
    background: radial-gradient(ellipse at bottom right, var(--ornament) 0%, var(--ornament-soft) 55%, rgba(255,255,255,0) 75%);
  }
  .tagline {
    position: absolute;
    left: 0; right: 0; top: 36px;
    text-align: center;
    font-family: "Courgette", cursive;
    font-size: 70px;
    line-height: 86px;
    color: var(--ink-title);
    font-weight: 400;
    letter-spacing: 1px;
  }
  .section-heading {
    position: absolute;
    left: 50px;
    font-family: "Courgette", cursive;
    font-weight: 400;
    color: var(--ink-body);
    display: flex;
    align-items: center;
    white-space: nowrap;
  }
  .section-heading::before {
    content: "";
    width: 20px; height: 20px;
    border-radius: 50%;
    background: var(--bullet);
    margin-right: 14px;
    flex: none;
  }
  .section-heading--offer { top: 232px; font-size: 46px; letter-spacing: 1.5px; }
  .section-heading--programs { top: 366px; font-size: 58px; letter-spacing: 3px; }
  .detail-list {
    position: absolute;
    left: 96px;
    list-style: none;
    font-family: "Libre Baskerville", serif;
    font-style: italic;
    font-weight: 700;
    color: var(--ink-body);
  }
  .detail-list li {
    position: relative;
    padding-left: 22px;
    white-space: nowrap;
  }
  .detail-list li::before {
    content: "";
    position: absolute;
    left: 0; top: 0.5em;
    width: 11px; height: 11px;
    border-radius: 50%;
    background: var(--bullet);
  }
  .detail-list--offer { top: 300px; font-size: 25px; line-height: 39px; letter-spacing: 1.5px; }
  .detail-list--programs { top: 440px; font-size: 23px; line-height: 34px; letter-spacing: 1px; }
</style>
</head>
<body>
  <main class="card">
    <div class="corner-flourish corner-flourish--top-left" role="img" aria-label="Blue swirl ornament in the top-left corner"></div>
    <div class="corner-flourish corner-flourish--bottom-right" role="img" aria-label="Blue swirl ornament in the bottom-right corner"></div>

    <h1 class="tagline">Promoting healthy living through<br>Fitness &amp; Nutrutition</h1>

    <h2 class="section-heading section-heading--offer">Need direction with your health &amp; fitness goals?</h2>
    <ul class="detail-list detail-list--offer">
      <li>Call now for your free 1 on 1<br>Personal Training Session with full consultation</li>
    </ul>

    <h2 class="section-heading section-heading--programs">Fitness Programs:</h2>
    <ul class="detail-list detail-list--programs">
      <li>Weight loss consults</li>
      <li>Female specific training</li>
      <li>Body sculpting</li>
      <li>HIIT</li>
      <li>Pre-Post natal</li>
    </ul>
  </main>
</body>
</html>
```